Sportdrink für Fussballer
Zielgruppe
WER WIR SIND?
Wir sind ein junges Label, das es sich zur Aufgabe macht, ambitionierte Fussballspieler aus dem Amateurbereich in Training & Spiel mit qualitativ hochwertiger Sportnahrung auszustatten.
Unsere Produkte richten sich an Sportler, die immer alles geben und mit unserer Unterstützung zu wahren Legenden auf dem Platz werden möchten.
Besucht auch gerne unseren Instagram Channel: torheldwerk
ZIELGRUPPE?
- Ambitionierte Amateurfussballspieler und -spielerinnen
- Alter: 16 - 30
- Fitnessaffin / Gesundheits & Ernährungsbewusst
- Trendy / hipster
- Bewusstsein für Mode, Ästhetik, Nachhaltigkeit
Aufgabenstellung
Liebe Designer!
Für unser Produkt - ein isotonisches Getränkepulver - benötigen wir eure Expertise bei der Gestaltung eines ansprechenden Etiketts.
Unser Getränkepulver wird in Dosen mit einer Höhe von 12,5 cm und einem Durchmesser von 9 cm angeboten (siehe Anhang für Beispieldose).
Die exakten Maße zur Gestaltung des Etiketts können der beigefügten Druckstandsskizze entnommen werden ( 4 farbig, Chromolux 80g / qm).
1) Generelle Anmerkungen zum gewünschten Design:
- Unser Produkt richtet sich ausschließlich an die Zielgruppe "Fussballer"
- Das Etikett sollte stilistisch auf jeden Fall in die Richtung "handmade / handcrafted" gehen (siehe Beispiele)
- Das Etikett sollte möglichst clean sein und nur vereinzelte Farbelemente enthalten (idealerweise weißer oder schwarzer Hintergrund)
- Das Logo sollte das Kernelement des Etiketts sein (siehe Fox Hall)
- Zur Besseren Visualisierung sollte jedem 2D Entwurf auch ein 3D Entwurf beigefügt werden
2) Elemente auf der Vorderseite
- Logo (großflächige Darstellung) im "used-look" (abgesplittert, zerkratzt, etc…)
- Produktname: "Isotonisches Sportgetränk"
- Logos für folgende Produkteigenschaften:
o Echtes Fruchtpulver
o Keine künstlichen Zusatzstoffe
o Hergestellt in Deutschland
- Box oder Farbband für Geschmacksrichtung: "Zitrone/Limette" ( Sollte sich gut dafür eignen auch andere Geschmacksrichtungen darstellen zu können)
- Platzhalter für Grammangabe (200 bzw. 400 Gramm)
3) Elemente auf der Rückseite
- Text:
Die letzten Minuten laufen. Dein Wille ist ungebrochen aber jeder Sprint bringt deine Oberschenkel zum brennen. Du willst den Sieg, deine Muskeln nur noch die Eistonne. Laut einer Studie des KSV sind deine Energiereserven je nach Spielposition nach 60 bis 70 Minuten vollständig erschöpft.
Die Folgen:
x Unnötige Fehlpässe
x Fehlende Spritzigkeit

```html
<!DOCTYPE html>
<html lang="de">
<head>
<meta charset="utf-8">
<title>Isotonisches Sportgetränk – Etikett Rückseite</title>
<link rel="stylesheet" href="https://fonts.googleapis.com/css2?family=Permanent+Marker&family=Roboto:wght@400;500;700&display=swap">
<style>
  :root {
    --page: #ececec;
    --label: #ffffff;
    --ink: #1a1a1a;
    --ink-soft: #4a4a4a;
    --accent: #f2e600;
    --rule: #2a2a2a;
  }
  * { box-sizing: border-box; margin: 0; padding: 0; }
  html, body { width: 1046px; height: 1200px; overflow: hidden; }
  body {
    background: var(--page);
    font-family: "Roboto", Arial, sans-serif;
    color: var(--ink);
    display: flex; align-items: center; justify-content: center;
  }
  .label {
    position: relative;
    width: 980px; height: 760px;
    background: var(--label);
    border-top: 14px solid var(--accent);
    border-bottom: 10px solid var(--accent);
    box-shadow: 0 2px 10px rgba(0,0,0,.12);
    display: grid;
    grid-template-columns: 1fr 1fr;
    column-gap: 60px;
    padding: 42px 46px 30px;
  }
  .label::before {
    content: ""; position: absolute; left: 0; right: 0; top: 12px;
    height: 3px; background: var(--accent);
  }
  .column { display: flex; flex-direction: column; }

  .brush-heading {
    display: inline-block;
    align-self: flex-start;
    background: var(--ink);
    color: var(--accent);
    font-family: "Permanent Marker", cursive;
    font-size: 25px; line-height: 1.02;
    text-transform: uppercase;
    padding: 8px 18px 6px 14px;
    clip-path: polygon(1% 6%, 97% 0, 100% 48%, 98% 100%, 3% 95%, 0 52%);
    margin-bottom: 16px;
  }
  .brush-heading.small { font-size: 20px; padding: 6px 14px 4px 12px; }

  .nutrition {
    width: 100%; border-collapse: collapse;
    border: 1.5px solid var(--rule);
    font-size: 11px;
  }
  .nutrition th, .nutrition td {
    text-align: left; padding: 3px 6px;
    border-left: 1px solid var(--rule);
  }
  .nutrition th { font-weight: 700; border-bottom: 1px solid var(--rule); }
  .nutrition tr.section th { border-top: 1.5px solid var(--rule); }
  .nutrition td:first-child, .nutrition th:first-child { width: 46%; }

  .fineprint { font-size: 10.5px; line-height: 1.45; color: var(--ink-soft); margin-top: 12px; }
  .fineprint em { font-style: italic; }

  .social-call {
    font-family: "Permanent Marker", cursive;
    font-size: 30px; letter-spacing: 1px;
    text-transform: uppercase; margin-top: 24px;
  }
  .social-row {
    display: flex; align-items: center; gap: 18px; margin-top: 12px;
    font-family: "Permanent Marker", cursive; font-size: 19px;
  }
  .social-handle { display: flex; align-items: center; gap: 8px; }
  .social-handle .dot { width: 14px; height: 14px; background: var(--ink); }
  .imprint { font-size: 10px; color: var(--ink-soft); margin-top: 14px; }

  .body-text { font-size: 11.5px; line-height: 1.5; }
  .body-text + .body-text { margin-top: 10px; }
  .body-text strong { font-weight: 700; }
  .divider { height: 1px; background: #bbb; margin: 16px 0; }

  .consequences { list-style: none; margin-bottom: 18px; }
  .consequences li {
    display: flex; align-items: center; gap: 10px;
    font-size: 11.5px; padding: 4px 0;
  }
  .consequences li::before {
    content: ""; width: 11px; height: 11px; background: var(--accent);
    border: 1px solid #cfc300; flex: none;
  }
</style>
</head>
<body>
  <main class="label">
    <section class="column">
      <h2 class="brush-heading">Nährwerttabelle &amp;<br>Inhaltsstoffe</h2>
      <table class="nutrition">
        <tr><th>Nährwerte</th><th>pro Portion (24g)</th><th>pro 100g</th></tr>
        <tr><td>Energie</td><td>335 kJ / 80 kcal</td><td>1334 kJ / 320 kcal</td></tr>
        <tr><td>Fett (g)</td><td>0</td><td>0</td></tr>
        <tr><td>davon gesättigte Fettsäuren (g)</td><td>0</td><td>0</td></tr>
        <tr><td>Kohlenhydrate (g)</td><td>21</td><td>84</td></tr>
        <tr><td>davon Zucker (g)</td><td>20</td><td>80</td></tr>
        <tr><td>Eiweiß (g)</td><td>0</td><td>0</td></tr>
        <tr><td>Natrium (mg)</td><td>900</td><td>3600</td></tr>
        <tr class="section"><th>Mineralstoffe</th><th>pro Portion (24g)</th><th>in % NRV</th></tr>
        <tr><td>Kalium</td><td>350 mg</td><td>16%</td></tr>
        <tr><td>Magnesium</td><td>28 mg</td><td>36%</td></tr>
      </table>
      <p class="fineprint">Zutaten: Fruchtpulver, Traubenzucker, Natriumcitrat, Zitronensäure, Maltodextrin, Zitronensaft, Limettensaft, Kaliumcitrat, Magnesiumcitrat, Meersalz.</p>
      <p class="fineprint"><em>Außerhalb der Reichweite von kleinen Kindern aufbewahren. Die empfohlene tägliche Verzehrmenge darf nicht überschritten werden. Nahrungsergänzungsmittel sind kein Ersatz für eine ausgewogene und abwechslungsreiche Ernährung. Kühl und trocken aufbewahren.</em></p>
      <p class="social-call">Stay tuned und folge uns auf</p>
      <div class="social-row">
        <span>www.torheldwerk.de</span>
        <span class="social-handle"><span class="dot"></span>torheldwerk</span>
      </div>
      <p class="imprint">Torheldwerk Sport-Commerce · Am Musterweg 6 · 80800 Musterstadt</p>
    </section>

    <section class="column">
      <h2 class="brush-heading">Zubereitung &amp;<br>Verzehrempfehlung</h2>
      <p class="body-text"><strong>Die Zubereitung ist easy:</strong><br>Je nach Vorliebe 24g Pulver in 400 bis 500 ml Wasser einrühren und fertig!</p>
      <p class="body-text">Für eine optimale Flüssigkeits- und Energiezufuhr empfehlen wir bereits beim Aufwärmen mit dem Trinken zu beginnen. Die nächste Belastung sollte dann im Abstand von 1 Stunde folgen.</p>
      <div class="divider"></div>
      <p class="body-text">Die letzten Minuten laufen. Dein Wille ist ungebrochen aber jeder Sprint bringt deine Oberschenkel zum brennen. Du willst den Sieg, deine Muskeln nur noch die Eistonne. Laut einer Studie des KSV sind deine Energiereserven je nach Spielposition nach 60 bis 70 Minuten vollständig erschöpft.</p>
      <div class="divider"></div>
      <h3 class="brush-heading small">Die Folgen</h3>
      <ul class="consequences">
        <li>Unnötige Fehlpässe</li>
        <li>Fehlende Spritzigkeit</li>
        <li>Schwaches Zweikampfverhalten</li>
        <li>Mangelnde Konzentration</li>
      </ul>
      <p class="body-text"><strong>Um deine Speicher schnell wieder aufzufüllen</strong></p>
      <p class="body-text">Nachdem uns die üblichen Sportgetränke zu süß waren, haben wir es uns zur Aufgabe gemacht, es besser zu machen. Dabei verzichten wir bewusst auf künstliche Zusatzstoffe und bedienen uns stattdessen echter Fruchtpulver. Unser besonderes Highlight verarbeiten wir für deine Geschmacksknospen am Ende des Spiels.</p>
    </section>
  </main>
</body>
</html>
```